Need a business card design for a new business

The business is going to be called "The Maple Lectern" - it is an online training company that provides Instructor Lead training to students at any destination in the world
The reference to cloud is the internet and classroom reference will be a computer at the students and instructors end

We will need a Web site and stationary and advertising material developed over time but for now require the business cards only

So if we are happy with the business card then we will use the same designers for the other requirments of the business as it evolves

Industry/Entity Type

Advertising

```html
<!DOCTYPE html>
<html lang="en">
<head>
<meta charset="utf-8">
<title>The Maple Lectern – Business Card</title>
<link rel="stylesheet" href="https://fonts.googleapis.com/css2?family=Arimo:wght@400;700&family=Della+Respira&display=swap">
<style>
  :root {
    --page: #f2f0e8;
    --card: #000000;
    --card-edge: #8a8a8a;
    --white: #ffffff;
    --teal: #74c8bb;
    --name-grey: #9a9a9a;
    --detail-grey: #c4c4c4;
    --font-brand: "Della Respira", serif;
    --font-body: "Arimo", sans-serif;
  }
  * { box-sizing: border-box; margin: 0; padding: 0; }
  html, body { width: 1200px; height: 1200px; overflow: hidden; }
  body {
    background: var(--page);
    position: relative;
    font-family: var(--font-body);
  }
  .card {
    position: absolute;
    left: 250px;
    width: 700px;
    height: 408px;
    background: var(--card);
  }
  .card--front { top: 60px; }
  .card--back { top: 700px; border: 2px solid var(--card-edge); }

  .brand {
    position: absolute;
    display: flex;
    align-items: center;
    font-family: var(--font-brand);
    color: var(--white);
    white-space: nowrap;
  }
  .brand__dot {
    border-radius: 50%;
    background: var(--teal);
    flex: none;
  }
  .card--front .brand {
    left: 0; right: 0; top: 150px;
    justify-content: center;
    gap: 24px;
    font-size: 52px;
  }
  .card--front .brand__dot { width: 60px; height: 60px; }
  .card--back .brand {
    right: 40px; top: 60px;
    gap: 14px;
    font-size: 26px;
  }
  .card--back .brand__dot { width: 30px; height: 30px; }

  .holder {
    position: absolute;
    left: 38px; top: 28px;
  }
  .holder__name {
    font-weight: 700;
    font-size: 38px;
    color: var(--name-grey);
    letter-spacing: 1px;
  }
  .holder__title {
    margin-left: 134px;
    font-size: 26px;
    color: var(--detail-grey);
    line-height: 1;
  }
  .contact {
    position: absolute;
    left: 36px; top: 172px;
    list-style: none;
    font-size: 25px;
    line-height: 34px;
    color: var(--detail-grey);
  }
</style>
</head>
<body>
  <section class="card card--front" aria-label="Card front">
    <div class="brand"><span class="brand__dot"></span>The Maple Lectern</div>
  </section>

  <section class="card card--back" aria-label="Card back">
    <div class="holder">
      <p class="holder__name">Dana Whitlow</p>
      <p class="holder__title">manger</p>
    </div>
    <div class="brand"><span class="brand__dot"></span>The Maple Lectern</div>
    <ul class="contact">
      <li>Phone: 555-201-4870</li>
      <li>Fax: 555-201-4871</li>
      <li>Email: dana@maplelectern.com</li>
      <li>1217 Birchwood Ln.</li>
      <li>Millbrook, IA 50312</li>
      <li>www.TheMapleLectern.com</li>
    </ul>
  </section>
</body>
</html>
```